LLC needs a business card design that emphasizes consulting and expert witness in upstream oil and g

I need a business card design for my company called Kelvora Consultative Service, LLC. My expertise is in oil and gas upstream operations management to optimize performance and also as an expert witness for law firms in oil and gas upstream operations litigation.
The final design should communicate knowledge and hands-on experience as well as trust. (Kelvora means rope or lasso. Perhaps "Kelvora" should be in the form of a rope.) I do not like the color green in any shade. My first preference would be some shade of blue.
Oil And Gas

```html
<!DOCTYPE html>
<html lang="en">
<head>
<meta charset="utf-8">
<title>Kelvora Consultative Service, LLC — Business Card</title>
<link rel="stylesheet" href="https://fonts.googleapis.com/css2?family=Questrial&display=swap">
<style>
  :root {
    --bg: #e9e7e3;
    --card-black: #0b0c0e;
    --card-white: #ffffff;
    --brand-blue: #1f3f7a;
    --accent-red: #8e1c1f;
    --text-light: #e6e6e6;
    --text-muted: #b9b9b9;
  }
  * { box-sizing: border-box; margin: 0; padding: 0; }
  html, body { width: 1200px; height: 892px; overflow: hidden; }
  body {
    background: var(--bg);
    font-family: "Questrial", "Century Gothic", sans-serif;
    position: relative;
  }
  .card {
    position: absolute;
    left: 320px;
    width: 560px;
    height: 320px;
    border-radius: 26px;
    overflow: hidden;
    box-shadow: 0 10px 28px rgba(0,0,0,0.22);
  }
  .card--front { top: 86px; background: var(--card-black); }
  .card--back  { top: 486px; background: var(--card-black); }

  /* Front */
  .front__band {
    position: absolute;
    left: 0; right: 0;
    top: 62px;
    height: 150px;
    background: var(--card-white);
    display: flex;
    align-items: center;
    justify-content: center;
    gap: 14px;
  }
  .brand-dot {
    width: 14px; height: 14px;
    border-radius: 50%;
    background: var(--accent-red);
  }
  .brand-name {
    color: var(--brand-blue);
    font-size: 31px;
    font-weight: 400;
    letter-spacing: 0.3px;
  }

  /* Back */
  .back__top {
    position: absolute;
    left: 0; right: 0; top: 0;
    height: 150px;
    background: var(--card-white);
    display: flex;
    align-items: flex-end;
    padding: 0 0 18px 40px;
  }
  .back__top .brand-name { font-size: 26px; }
  .back__info {
    position: absolute;
    left: 0; right: 0; top: 150px; bottom: 0;
    display: flex;
    align-items: center;
    padding: 0 40px;
  }
  .person { width: 210px; text-align: right; padding-right: 26px; }
  .person__name { color: var(--text-light); font-size: 24px; }
  .person__role { color: var(--text-muted); font-size: 14px; margin-top: 4px; }
  .divider {
    width: 2px; height: 96px;
    background: var(--accent-red);
  }
  .contact { list-style: none; padding-left: 24px; }
  .contact li {
    color: var(--text-light);
    font-size: 14px;
    line-height: 22px;
  }
</style>
</head>
<body>
  <section class="card card--front" aria-label="Business card front">
    <div class="front__band">
      <span class="brand-dot"></span>
      <span class="brand-name">Kelvora Consultative Service, LLC</span>
    </div>
  </section>

  <section class="card card--back" aria-label="Business card back">
    <div class="back__top">
      <span class="brand-name">Kelvora Consultative Service, LLC</span>
    </div>
    <div class="back__info">
      <div class="person">
        <p class="person__name">Employee Name</p>
        <p class="person__role">Your Position</p>
      </div>
      <div class="divider"></div>
      <ul class="contact">
        <li>555-01200-00</li>
        <li>www.kelvoraconsultative.com</li>
        <li>hello@kelvoraconsultative.com</li>
        <li>0000 Harlow Rd, Tulsa, OK 00000</li>
      </ul>
    </div>
  </section>
</body>
</html>
```